Harbor Sushi & Steak Dinner Menu

I'm looking for a MENU design with a particular feel. I want to have a base template made that I can then use for future alterations to the menu; ie I can go in and change out different entrees as the menu changes but the template will remain the same. (Ideally it would be in an Apple Pages format.). Also ideally - dinner menu will occupy 2 pages 8.5 x 11. The restaurant's name is Harbor. It is a MODERN steak house that will also feature Sushi, a Raw Bar, Exquisite Cocktails and a sophisticated nightlife crowd. I have attached our LOGO, a secondary logo that we will be featuring throughout the project including on the menu cover (the gold U). Finally - I have attached the content that we would like to see. AGAIN - I REITERATE: High end dining and lounge atmosphere. A couple of restaurants / menus that I love are Corvellin in NYC and Marrowby Steakhouse in Long Island NY. Please do not duplicate - just trying to offer some suggestions.

Requirements
Must have
• A sophisticated and elegant feel without being stuffy or old.

```html
<!DOCTYPE html>
<html lang="en">
<head>
<meta charset="utf-8">
<title>Harbor Sushi &amp; Steak — Dinner Menu</title>
<link href="https://fonts.googleapis.com/css2?family=Signika:wght@400;600;700&display=swap" rel="stylesheet">
<style>
:root{
  --frame-top:#d8c993;
  --frame-bottom:#c1865f;
  --paper:#ffffff;
  --gold:#c5a56c;
  --gold-line:#c9a877;
  --ink:#161616;
  --accent:#e3163a;
  --ribbon-top:#d4bd8c;
  --ribbon-bottom:#b9714f;
}
*{margin:0;padding:0;box-sizing:border-box}
html,body{width:880px;height:1200px;overflow:hidden}
body{font-family:"Signika",sans-serif;color:var(--ink)}
.menu{position:relative;width:880px;height:1200px;background:linear-gradient(180deg,var(--frame-top),var(--frame-bottom))}
.paper{position:absolute;left:16px;top:16px;width:848px;height:1166px;background:var(--paper)}
.rule-frame{position:absolute;left:37px;top:38px;width:806px;height:1123px;border:2px solid var(--gold-line)}
.ribbon{position:absolute;left:395px;top:16px;width:92px;height:133px}
.ribbon-name{position:absolute;left:395px;top:70px;width:92px;text-align:center;color:#fff;font-weight:600;font-size:17px;letter-spacing:.5px}
.divider{position:absolute;left:440px;top:188px;width:2px;height:944px;background:var(--gold-line)}
.heading{position:absolute;font-weight:600;font-size:23px;color:var(--gold);letter-spacing:.6px;padding:0 3px 1px;border-bottom:1px solid var(--gold-line);line-height:26px}
.item{position:absolute;line-height:1}
.left{left:70px;width:346px}
.right{left:473px;width:338px}
.row{display:flex;align-items:flex-end;height:18px}
.name{font-weight:700;font-size:13.5px;letter-spacing:.3px;white-space:nowrap}
.name small{font-weight:400;font-size:12.5px;letter-spacing:0;margin-left:3px}
.leader{flex:1;border-bottom:1px dotted #555;margin:0 2px 4px 10px;min-width:20px}
.price{font-weight:600;font-size:21px;color:var(--gold);line-height:1;margin-bottom:-2px}
.desc{font-size:12px;line-height:13.5px;margin-top:2px}
.big .name{font-size:15px}
.big .desc{font-size:14.5px;line-height:14px}
.plain{font-weight:700;font-size:13.5px;letter-spacing:.3px;position:absolute;left:474px}
.accent{color:var(--accent)}
</style>
</head>
<body>
<main class="menu">
  <div class="paper"></div>
  <div class="rule-frame"></div>
  <svg class="ribbon" viewBox="0 0 92 133" aria-hidden="true">
    <defs><linearGradient id="rib" x1="0" y1="0" x2="0" y2="1"><stop offset="0" stop-color="var(--ribbon-top)"/><stop offset="1" stop-color="var(--ribbon-bottom)"/></linearGradient></defs>
    <polygon points="0,0 92,0 92,133 46,120 0,133" fill="url(#rib)"/>
  </svg>
  <div class="ribbon-name">Harbor</div>
  <div class="divider"></div>

  <!-- Sushi / Sashimi -->
  <h2 class="heading" style="left:116px;top:152px">SUSHI / SASHIMI</h2>
  <div class="item left" style="top:194px"><div class="row"><span class="name">TORO<small>blue fin tuna belly (gf)</small></span><span class="leader"></span><span class="price">$0.00</span></div></div>
  <div class="item left" style="top:220px"><div class="row"><span class="name">EBI<small>cooked shrimp (gf)</small></span><span class="leader"></span><span class="price">$0.00</span></div></div>
  <div class="item left" style="top:248px"><div class="row"><span class="name">HAMACHI<small>yellowtail (gf)</small></span><span class="leader"></span><span class="price">$0.00</span></div></div>
  <div class="item left" style="top:274px"><div class="row"><span class="name">UNI<small>sea urchin (gf)</small></span><span class="leader"></span><span class="price">$0.00</span></div></div>
  <div class="item left" style="top:300px"><div class="row"><span class="name">HIRAME<small>fluke (gf)</small></span><span class="leader"></span><span class="price">$0.00</span></div></div>
  <div class="item left" style="top:330px"><div class="row"><span class="name">UNAGI<small>fresh water eel (gf)</small></span><span class="leader"></span><span class="price">$0.00</span></div></div>
  <div class="item left" style="top:357px"><div class="row"><span class="name">SAKE<small>salmon (gf)</small></span><span class="leader"></span><span class="price">$0.00</span></div></div>
  <div class="item left" style="top:387px"><div class="row"><span class="name">MADAI<small>red snapper (gf)</small></span><span class="leader"></span><span class="price">$0.00</span></div></div>
  <div class="item left" style="top:415px"><div class="row"><span class="name">MAGURO<small>tuna (gf)</small></span><span class="leader"></span><span class="price">$0.00</span></div></div>

  <!-- Sushi Platters -->
  <h2 class="heading" style="left:116px;top:457px">SUSHI PLATTERS</h2>
  <div class="item left" style="top:499px"><div class="row"><span class="name">SMALL</span><span class="leader"></span><span class="price">$0.00</span></div><p class="desc">Five Pieces assorted sushi, nine pieces sashimi,<br>spicy tuna roll (gf)</p></div>
  <div class="item left" style="top:563px"><div class="row"><span class="name">LARGE</span><span class="leader"></span><span class="price">$0.00</span></div><p class="desc">Eight Pieces assorted sushi, eighteen pieces<br>of sashimi, alaskan roll, rainbow roll (gf)</p></div>

  <!-- Classic Rolls -->
  <h2 class="heading" style="left:112px;top:640px">CLASSIC ROLLS</h2>
  <div class="item left" style="top:688px"><div class="row"><span class="name">YELLOWTAIL</span><span class="leader"></span><span class="price">$0.00</span></div><p class="desc">inside out roll with scallions (gf)</p></div>
  <div class="item left" style="top:737px"><div class="name">SPICY TUNA OR SALMON OR</div><div class="row"><span class="name">YELLOWTAIL</span><span class="leader"></span><span class="price">$0.00</span></div><p class="desc">spicy mayo</p></div>
  <div class="item left" style="top:803px"><div class="row"><span class="name">CALIFORNIA</span><span class="leader"></span><span class="price">$0.00</span></div><p class="desc">crab meat, cucumber and avocado (gf)</p></div>
  <div class="item left big" style="top:852px"><div class="row"><span class="name">VEGETABLE</span><span class="leader"></span><span class="price">$0.00</span></div><p class="desc">avocado, cucumber,<br>asparagus and pickled reddish (gf)</p></div>
  <div class="item left big" style="top:921px"><div class="row"><span class="name">SPIDER</span><span class="leader"></span><span class="price">$0.00</span></div><p class="desc">soft shell crab<br>and avocado with eel sauce</p></div>
  <div class="item left big" style="top:991px"><div class="row"><span class="name">SHRIMP TEMPURA</span><span class="leader"></span><span class="price">$0.00</span></div><p class="desc">deep fried tempura shrimp<br>and eel sauce</p></div>
  <div class="item left big" style="top:1056px"><div class="row"><span class="name">ALASKAN</span><span class="leader"></span><span class="price">$0.00</span></div><p class="desc">salmon and avocado (gf)</p></div>

  <!-- Special Rolls -->
  <h2 class="heading" style="left:534px;top:154px">SPECIAL ROLLS</h2>
  <div class="item right" style="top:195px"><div class="row"><span class="name">THE HARBOR</span><span class="leader"></span><span class="price">$0.00</span></div><p class="desc">tuna, salmon, yellowtail, avocado,<br>spicy mayo, soy bean paper</p></div>
  <div class="item right" style="top:257px"><div class="row"><span class="name">KING CRAB RAINBOW</span><span class="leader"></span><span class="price">$0.00</span></div><p class="desc">king crab, avocado, cucumbers,<br>assorted fish on top</p></div>
  <div class="item right" style="top:322px"><div class="row"><span class="name">EMPRESS</span><span class="leader"></span><span class="price">$0.00</span></div><p class="desc">Shrimp tempura, spicy tuna on top,<br>eel sauce, spicy mayo</p></div>
  <div class="item right" style="top:389px"><div class="row"><span class="name">SPICY GIRL</span><span class="leader"></span><span class="price">$0.00</span></div><p class="desc">Spicy crunchy crab meat, cucumber,<br>shrimp on top</p></div>
  <div class="item right" style="top:457px"><div class="row"><span class="name">DRAGON</span><span class="leader"></span><span class="price">$0.00</span></div><p class="desc">Eel, cucumber, avocado,<br>and tobiko on top, eel sauce</p></div>
  <div class="item right" style="top:526px"><div class="row"><span class="name">YUMMY</span><span class="leader"></span><span class="price">$0.00</span></div><p class="desc">spicy crunchy salmon, avocado,<br>mango and salmon on top</p></div>
  <div class="item right" style="top:597px"><div class="row"><span class="name">NO. 9</span><span class="leader"></span><span class="price">$0.00</span></div><p class="desc">Shrimp Tempura, avocado,<br>kani, spicy mayo, tobiko</p></div>
  <div class="item right" style="top:670px"><div class="row"><span class="name">SUNRISE ROLL</span><span class="leader"></span><span class="price">$0.00</span></div><p class="desc">spicy crunchy tuna and avocado,<br>spicy crunchy salmon on top</p></div>

  <!-- Seafood Raw Bar -->
  <h2 class="heading" style="left:529px;top:758px">SEAFOOD RAW BAR</h2>
  <div class="plain" style="top:807px">LOBSTER COCKTAIL</div>
  <div class="plain" style="top:830px">SHRIMP COCKTAIL</div>
  <div class="plain" style="top:853px">CLAMS ON THE HALF SHELL</div>
  <div class="plain" style="top:877px">OYSTERS ON THE HALF SHELL</div>
  <div class="plain" style="top:900px">COLOSSAL CRAB COCKTAIL</div>
  <div class="item right" style="top:933px"><div class="name accent">RAW BAR PLATE FOR ONE:</div><p class="desc">Two Shrimp, Half of a One Pound Lobster, Two Clams,<br>One East Coast Oyster, One West Coast Oyster</p></div>

  <!-- Seafood Platters -->
  <h2 class="heading" style="left:529px;top:1010px">SEAFOOD PLATTERS (GF)</h2>
  <div class="plain" style="top:1058px;line-height:17px">SHRIMP, OYSTERS, CLAMS,<br>LOBSTER AND CRAB</div>
  <div class="plain accent" style="top:1103px">LARGE OR COLOSSAL</div>
</main>
</body>
</html>
```